Business cards to launch an education platform

Hi,
I am looking at having new business cards designed.
I am a startup, developing a web platform for schools and university, the education world. It's an online assessment system.
I would like a card that looks classy, and that is using the colors and the font of my logo.

I have attached:
1) my logo
2) A business card that I have designed quickly so you can have all the information required in the card, but I really don't like it.
3) The font that I am using (Lato Regular) to design my web platform
4) Some screenshots of my web platform so you can have a look at the style that I have.

Target Market(s)

Major market: Education system: Schools and university
Minor markets: Business in general

Industry/Entity Type

Business

Contact Information for Business Card

Lydia Marsh
Director

M: 0437 681 902
E: lydia.marsh@copperLeafSystems.com.au

Requirements
Must have
• The colors of my logo

```html
<!DOCTYPE html>
<html lang="en">
<head>
<meta charset="utf-8">
<title>Copper Leaf Systems – Business Cards</title>
<link rel="stylesheet" href="https://fonts.googleapis.com/css2?family=Lato:wght@400;700&display=swap">
<style>
  :root {
    --backdrop: #2b2d30;
    --card: #1c2229;
    --card-edge: #232a32;
    --blue-bright: #2aa6e4;
    --blue-mid: #1f86d2;
    --blue-deep: #1e5c9c;
    --line: #1f9ad9;
  }
  * { margin: 0; padding: 0; box-sizing: border-box; }
  html, body {
    width: 1200px; height: 1189px; overflow: hidden;
    background: var(--backdrop);
    font-family: "Lato", Arial, sans-serif;
  }
  .stage { position: relative; width: 1200px; height: 1189px; }
  .card {
    position: absolute; left: 150px; width: 900px; height: 514px;
    background: var(--card);
    border: 1px solid var(--card-edge);
    border-radius: 28px;
    box-shadow: 0 18px 40px rgba(0,0,0,.55);
    overflow: hidden;
  }
  .card--front { top: 50px; }
  .card--back { top: 620px; }

  .brand { position: absolute; display: flex; align-items: center; gap: 22px; }
  .brand__mark {
    width: 86px; height: 86px; background: var(--blue-mid); border-radius: 6px;
  }
  .brand__name {
    color: var(--blue-mid); font-weight: 400;
    font-size: 44px; letter-spacing: 5px; line-height: 1.1;
    text-transform: uppercase;
  }
  .card--front .brand { left: 210px; top: 214px; }

  .card--back .brand { left: 60px; top: 60px; }
  .card--back .brand__name { font-size: 40px; }

  .holder { position: absolute; right: 60px; top: 200px; text-align: right; }
  .holder__name { color: var(--blue-deep); font-size: 34px; font-weight: 700; }
  .holder__role { color: var(--blue-mid); font-size: 22px; margin-top: 2px; }

  .divider {
    position: absolute; left: 60px; right: 60px; top: 292px;
    height: 2px; background: var(--line);
  }

  .website {
    position: absolute; right: 60px; top: 322px;
    color: var(--blue-mid); font-size: 22px;
  }

  .contacts { position: absolute; left: 60px; bottom: 50px; list-style: none; }
  .contacts li {
    display: flex; align-items: center; gap: 14px;
    color: var(--blue-deep); font-size: 24px; margin-top: 10px;
    white-space: nowrap;
  }
  .contacts svg { width: 32px; height: 32px; flex: none; }
</style>
</head>
<body>
<main class="stage">

  <section class="card card--front" aria-label="Card front">
    <div class="brand">
      <span class="brand__mark"></span>
      <span class="brand__name">Copper Leaf<br>Systems</span>
    </div>
  </section>

  <section class="card card--back" aria-label="Card back">
    <div class="brand">
      <span class="brand__mark"></span>
      <span class="brand__name">Copper Leaf<br>Systems</span>
    </div>

    <div class="holder">
      <p class="holder__name">Lydia Marsh</p>
      <p class="holder__role">Director</p>
    </div>

    <div class="divider"></div>

    <p class="website">www.copperleafsystems.com.au</p>

    <ul class="contacts">
      <li>
        <svg viewBox="0 0 32 32" aria-hidden="true">
          <rect x="1" y="1" width="30" height="30" rx="4" fill="var(--blue-bright)"/>
          <rect x="10" y="5" width="12" height="22" rx="2" fill="none" stroke="var(--card)" stroke-width="2"/>
          <rect x="12.5" y="8" width="7" height="6" fill="var(--card)"/>
          <circle cx="16" cy="23" r="1.5" fill="var(--card)"/>
        </svg>
        0437 681 902
      </li>
      <li>
        <svg viewBox="0 0 32 32" aria-hidden="true">
          <rect x="1" y="1" width="30" height="30" rx="4" fill="var(--blue-bright)"/>
          <rect x="5" y="9" width="22" height="15" fill="none" stroke="var(--card)" stroke-width="2"/>
          <path d="M5 9 L16 18 L27 9 M5 24 L13 16 M27 24 L19 16" fill="none" stroke="var(--card)" stroke-width="2"/>
        </svg>
        lydia.marsh@copperLeafSystems.com.au
      </li>
    </ul>
  </section>

</main>
</body>
</html>
```